A Hair, Beauty and Nails Wholesalers Needs a Business Card Design

We need a business card design for our company which is being passed from parents to daughter, so we wont to re-launch the company with an updated, modern, sophisticated, elegant, chic and fresh look which still incorporates the original colour scheme of Hot Pink, Dark Grey and White. The original logo which is attached can be used on the card but we would like to see some designs with the logo and some without, as we have not yet decided if we want the logo on the card. The name of our company is 'Velmora Supplies' and the name of our website is VelmoraGlowandPolish.example.au. We specialise in supplying a massive range of Hair, Beauty and Nail products to the industry. We are based in QLD, Australia but ship many orders via our website all across Australia.

```html
<!DOCTYPE html>
<html lang="en">
<head>
<meta charset="utf-8">
<title>Velmora Supplies – Business Card</title>
<link rel="stylesheet" href="https://fonts.googleapis.com/css2?family=Arimo:wght@400&family=Tinos:wght@400&display=swap">
<style>
  :root {
    --hot-pink: #ec2a8f;
    --hot-pink-light: #f03d9c;
    --dark-grey: #2f3b3d;
    --white: #ffffff;
    --backdrop: #e9e6e3;
  }
  * { box-sizing: border-box; margin: 0; padding: 0; }
  html, body { width: 1200px; height: 914px; overflow: hidden; }
  body {
    background: var(--backdrop);
    font-family: "Arimo", Arial, sans-serif;
    position: relative;
  }
  .card {
    position: absolute;
    left: 270px;
    width: 660px;
    height: 400px;
    background: var(--white);
    box-shadow: 0 6px 18px rgba(0,0,0,0.18);
    overflow: hidden;
  }
  .card--front { top: 40px; display: flex; }
  .card--back {
    top: 474px;
    display: flex;
    align-items: center;
    justify-content: center;
  }

  .brand-name {
    font-family: "Tinos", Georgia, serif;
    color: var(--hot-pink);
    white-space: nowrap;
  }

  /* Front face */
  .brand-side {
    width: 40%;
    display: flex;
    align-items: center;
    justify-content: center;
  }
  .brand-side .brand-name { font-size: 28px; }

  .details-side {
    width: 60%;
    background: linear-gradient(135deg, var(--hot-pink-light), var(--hot-pink));
    padding: 34px 26px 0 30px;
    color: var(--white);
  }
  .person-name {
    font-family: "Tinos", Georgia, serif;
    font-weight: 400;
    font-size: 30px;
    color: var(--dark-grey);
    line-height: 1.05;
  }
  .person-role {
    font-size: 15px;
    color: var(--white);
    margin-top: 2px;
  }
  .company-name {
    font-weight: 400;
    font-size: 24px;
    color: var(--dark-grey);
    margin-top: 26px;
  }
  .contact-list {
    list-style: none;
    margin-top: 24px;
    display: grid;
    grid-template-columns: 20px 1fr;
    column-gap: 14px;
    row-gap: 10px;
    font-size: 14px;
    line-height: 1.25;
  }
  .contact-list svg { width: 17px; height: 17px; fill: var(--dark-grey); }

  /* Back face */
  .card--back .brand-name { font-size: 44px; }
</style>
</head>
<body>

<section class="card card--front" aria-label="Business card front">
  <div class="brand-side">
    <div class="brand-name">Velmora Supplies</div>
  </div>
  <div class="details-side">
    <h1 class="person-name">Maren Ashdale</h1>
    <p class="person-role">Manager</p>
    <h2 class="company-name">Velmora Supplies</h2>
    <ul class="contact-list">
      <li><svg viewBox="0 0 24 24" aria-hidden="true"><path d="M12 3 2 12h3v9h5v-6h4v6h5v-9h3z"/></svg></li>
      <li>27 Larkspur Lane<br>BRINDALE, QLD, 4999</li>
      <li><svg viewBox="0 0 24 24" aria-hidden="true"><path d="M6.6 10.8a15 15 0 0 0 6.6 6.6l2.2-2.2a1 1 0 0 1 1-.25 11.4 11.4 0 0 0 3.6.57 1 1 0 0 1 1 1V20a1 1 0 0 1-1 1A17 17 0 0 1 3 4a1 1 0 0 1 1-1h3.5a1 1 0 0 1 1 1c0 1.25.2 2.45.57 3.57a1 1 0 0 1-.25 1z"/></svg></li>
      <li>(07) 5550 0142</li>
      <li><svg viewBox="0 0 24 24" aria-hidden="true"><path d="M2 5h20v14H2zm2 2v.5l8 5 8-5V7l-8 5z"/></svg></li>
      <li>admin@velmoraglowandpolish.example.au</li>
      <li><svg viewBox="0 0 24 24" aria-hidden="true"><circle cx="12" cy="12" r="9" fill="none" stroke="#2f3b3d" stroke-width="2"/><path d="M3 12h18M12 3c3 3 3 15 0 18M12 3c-3 3-3 15 0 18" fill="none" stroke="#2f3b3d" stroke-width="1.6"/></svg></li>
      <li>www.velmoraglowandpolish.example.au</li>
    </ul>
  </div>
</section>

<section class="card card--back" aria-label="Business card back">
  <div class="brand-name">Velmora Supplies</div>
</section>

</body>
</html>
```